Werbesprüche und/oder Design für Schmutzschleusen
Zielgruppe
Die KLV GmbH ist als Schienenpersonennahverkehrsunternehmen grenzüberschreitend zwischen der Schweiz und Deutschland unterwegs.
Unsere Züge sollen nun in den Eingangsbereichen mit Teppichen (Schmutzschleusen) ausgestattet werden.
Die Zielgruppe sind unsere Fahrgäste; also Pendler, Studenten, Schüler, Touristen etc...
Aufgabenstellung
Der Teppich ist 142 x 262 cm groß. Die schmalen Seiten liegen jeweils an den Ein- und Ausstiegen.
Der Großteil des Teppichs soll recht dunkel gehalten werden, so dass Schmutzablagerungen nicht gleich ersichtlich sind: d.h. dunkelgrau, dunkelrot, dunkelblau, dunkelgrün etc....
Da einfarbig monoton wirkt, beabsichtigen wir einen kreativen Spruch/Grafik/Piktogramm etc. zu integrieren, welche/s sich vom Hintergrund farblich abhebt.
Die Fahrgäste sollen mit einem Schmunzeln in den Zug einsteigen bzw. sich wohlfühlen.
Der Spruch und/oder die Grafik sollen von beiden Einstiegsseiten (schmale Seite mit 142 cm) gut gelesen werden können.
Unsere Logos können, müssen aber nicht verwendet werden.
Da wir in verschiedenen Regionen unterwegs sind, bitte entweder das KLV-Logo alleinig verwenden oder in folgenden Kombinationen: KLV + moorfink-Logo oder KLV + Talbahn-Logo.

```html
<!DOCTYPE html>
<html lang="de">
<head>
<meta charset="utf-8">
<title>KLV Schmutzschleuse – Zug um Zug ans Ziel</title>
<link rel="stylesheet" href="https://fonts.googleapis.com/css2?family=Source+Sans+3:ital,wght@0,700;1,600;1,700&display=swap">
<style>
  :root {
    --tile-dark: #43535e;
    --tile-light: #637f8c;
    --text-white: #ffffff;
    --brand-red: #e30613;
  }
  html, body {
    margin: 0;
    padding: 0;
    width: 1200px;
    height: 2212px;
    overflow: hidden;
    background: var(--tile-light);
  }
  .mat {
    position: relative;
    width: 1200px;
    height: 2212px;
    overflow: hidden;
  }
  .checkerboard {
    position: absolute;
    inset: 0;
    display: block;
  }
  .entry-side {
    position: absolute;
    inset: 0;
    color: var(--text-white);
    font-family: "Source Sans 3", "Myriad Pro", sans-serif;
  }
  .entry-side--far {
    transform: rotate(180deg);
  }
  .slogan {
    position: absolute;
    left: 110px;
    top: 1398px;
    margin: 0;
    font-size: 150px;
    font-style: italic;
    font-weight: 600;
    line-height: 164px;
    letter-spacing: -1px;
  }
  .tagline {
    position: absolute;
    left: 112px;
    top: 1788px;
    margin: 0;
    font-size: 60px;
    font-style: italic;
    font-weight: 700;
    line-height: 1;
  }
  .brand {
    position: absolute;
    left: 110px;
    top: 2036px;
    display: flex;
    align-items: center;
    gap: 24px;
  }
  .brand-square {
    width: 62px;
    height: 62px;
    background: var(--brand-red);
  }
  .brand-name {
    font-size: 64px;
    font-weight: 700;
    line-height: 1;
    color: var(--text-white);
  }
</style>
</head>
<body>
<main class="mat">
  <svg class="checkerboard" width="1200" height="2212" viewBox="0 0 1200 2212" aria-hidden="true">
    <rect width="1200" height="2212" fill="var(--tile-light)"/>
    <g fill="var(--tile-dark)">
      <rect x="0" y="0" width="300" height="316"/>
      <rect x="600" y="0" width="300" height="316"/>
      <rect x="300" y="316" width="300" height="316"/>
      <rect x="900" y="316" width="300" height="316"/>
      <rect x="0" y="632" width="300" height="316"/>
      <rect x="600" y="632" width="300" height="316"/>
      <rect x="300" y="948" width="300" height="316"/>
      <rect x="900" y="948" width="300" height="316"/>
      <rect x="0" y="1264" width="300" height="316"/>
      <rect x="600" y="1264" width="300" height="316"/>
      <rect x="300" y="1580" width="300" height="316"/>
      <rect x="900" y="1580" width="300" height="316"/>
      <rect x="0" y="1896" width="300" height="316"/>
      <rect x="600" y="1896" width="300" height="316"/>
    </g>
  </svg>

  <section class="entry-side entry-side--near">
    <h1 class="slogan">Zug um Zug<br>ans Ziel.</h1>
    <p class="tagline">Wie im Spiel.</p>
    <div class="brand">
      <span class="brand-square"></span>
      <span class="brand-name">KLV</span>
    </div>
  </section>

  <section class="entry-side entry-side--far" aria-hidden="true">
    <p class="slogan">Zug um Zug<br>ans Ziel.</p>
    <p class="tagline">Wie im Spiel.</p>
    <div class="brand">
      <span class="brand-square"></span>
      <span class="brand-name">KLV</span>
    </div>
  </section>
</main>
</body>
</html>
```